CBD Boutique Business Card Needed

We are in need of a business card to reflect the direction of our latest products. We are a fully organic company in which our store and products are very heavy in wood and "natural" components. We decided to bring color into one of our brands and immediately knew this is where we needed to go.

We are NOT a cash grab CBD company. We could have done this wrong, slapped a label on a shit product and left it like that. I am passionate about sharing my experience with other veterans and opening a store and making it a comfortable place for others to come and see if they can have the same experience.

Target Market(s)

We are a dual market company. We do have a beauty line that will cover the costs of the majority of our business. But we also heavily cater to veterans and first responders. I am a veteran and this is how I found out about CBD. So the marketing needs to bring in our higher end beauty clientele but also be able to not put off our customers that readily need this.

Contact Information for Business Card

What we are looking for is a light, professional, boutique design that is is neither quite feminine or masculine. Attached is a picture of a store in Portland that we asked our store designer to get her inspiration from. But all natural wood and black outlines are what is mostly in there.

Attached are the following files:

Logo: An AI file with how we have our logo. I do not understand AI and have no idea why the letters are individual. The font is Adam. OLU is the logo and Tonics of Vigor is our tagline.

KM Vantage (front and back) cards I did originally found at a trade show that I absolutely loved...while it is mostly there and I would still be happy with them but it is me pretending to be you. I understand I am not and there is probably a lot wrong that all of you would see instantly and this is why I am here.

Dropper Bottle: This is our final product mock up

Water Color: I am semi flexible here. This water color is slightly different on every level of our brand. The color itself can change...we are not stuck on THIS particular one. If you happen to make a new one that is similar in style and we use it...then I will happily commission you to change the rest on our next product run. I am pretty sure you can use this statement as evidence later . =) .

But seriously, we heavily believe in pay it forward and will work with anyone here that may have a vision bigger than ours. The winner of this contest will get preferential consideration on our marketing materials (need letterhead etc. next, as well as a brochure, and website) so three more projects coming down the pipeline.

Information to use for your mockup is contained on the card images I have included. I would prefer CBD for wellness CBD for life to be more prominent. No where else on the card do we have CBD mentioned.

Font styles to use
Sans Serif

Colors

Designer to choose colors to be used in the design.

Requirements
Must have
• Double Sided
• Front: OLU logo on front of card will be raised embossed. Background is watercolor. One has been provided. Others are up for consideration. If the rest of your design is incredible and I don't like your watercolor I will just ask to swap it.
• Back: Standard information. Not stuck on anything here. I LOVE clean minimal designs. The bleed on the card I provided is a luxury...
• Font for title and OLU is Adam. Everything else I prefer san serif or as clean as possible.
Nice to have
• I Need to incorporate Naturally Nurturing somewhere on the card. Bold but not intrusive.

```html
<!DOCTYPE html>
<html lang="en">
<head>
<meta charset="utf-8">
<title>OLU – Business Card</title>
<link rel="stylesheet" href="https://fonts.googleapis.com/css2?family=Source+Sans+3:wght@300;400;600&display=swap">
<style>
  :root {
    --backdrop: #b3b3b3;
    --card-light: #dcdedd;
    --card-dark: #222222;
    --wash-warm: #3a3128;
    --wash-cool: #2a2d30;
    --ink: #1f1f1f;
    --ink-soft: #3a3a3a;
    --silver: #9a9a9a;
    --gold: #c8a45e;
  }
  * { margin: 0; padding: 0; box-sizing: border-box; }
  html, body {
    width: 1200px; height: 800px; overflow: hidden;
    background: var(--backdrop);
    font-family: "Source Sans 3", Arial, sans-serif;
  }
  .stage { position: relative; width: 1200px; height: 800px; }
  .card {
    position: absolute; top: 192px;
    width: 240px; height: 418px;
    overflow: hidden;
  }
  .card--info { left: 299px; background: var(--card-light); color: var(--ink); }
  .card--brand { left: 599px; background: var(--card-dark); }

  .watercolor-wash {
    position: absolute; inset: 0;
    background:
      radial-gradient(ellipse 70% 45% at 25% 20%, var(--wash-warm) 0%, transparent 70%),
      radial-gradient(ellipse 60% 50% at 80% 75%, var(--wash-cool) 0%, transparent 70%),
      radial-gradient(ellipse 50% 35% at 60% 45%, #2c2925 0%, transparent 75%),
      var(--card-dark);
  }

  .wordmark {
    position: absolute; left: 38px;
    font-weight: 300; font-size: 82px; line-height: 1;
    letter-spacing: 6px;
  }
  .tagline {
    position: absolute; left: 40px;
    font-weight: 300; font-size: 14.5px; letter-spacing: 0.6px;
    text-transform: uppercase; white-space: nowrap;
  }
  .card--info .wordmark { top: 74px; color: var(--silver); }
  .card--info .tagline { top: 155px; color: var(--silver); }
  .card--brand .wordmark { top: 150px; left: 36px; color: var(--gold); }
  .card--brand .tagline { top: 232px; left: 38px; color: var(--gold); }

  .person { position: absolute; left: 40px; top: 206px; }
  .person__name { font-weight: 600; font-size: 15px; letter-spacing: 0.8px; text-transform: uppercase; }
  .person__role { font-size: 9.5px; letter-spacing: 0.4px; text-transform: uppercase; color: var(--ink-soft); margin-top: 3px; }

  .contacts { position: absolute; left: 40px; top: 256px; list-style: none; }
  .contacts li {
    display: flex; align-items: center; gap: 6px;
    font-size: 10px; line-height: 15.5px; color: var(--ink-soft);
  }
  .contacts svg { width: 8px; height: 8px; fill: var(--ink-soft); }

  .address {
    position: absolute; left: 40px; top: 310px;
    font-style: normal; font-size: 10px; line-height: 15.5px; color: var(--ink-soft);
  }
  .rule { position: absolute; left: 40px; top: 350px; width: 14px; height: 2px; background: var(--ink); }
  .motto {
    position: absolute; left: 40px; top: 358px;
    font-size: 13px; font-weight: 600; letter-spacing: 0.3px;
    color: var(--ink); white-space: nowrap;
  }
</style>
</head>
<body>
<main class="stage">
  <section class="card card--info" aria-label="Card back, contact details">
    <div class="wordmark">OLU</div>
    <div class="tagline">Tonics of Vigor</div>

    <div class="person">
      <div class="person__name">Nadia Calloway</div>
      <div class="person__role">Owner / CEO</div>
    </div>

    <ul class="contacts">
      <li>
        <svg viewBox="0 0 10 10" aria-hidden="true"><path d="M2 0.5 L3.8 2.6 L2.9 3.8 Q4 6 6.2 7.1 L7.4 6.2 L9.5 8 L8.2 9.5 Q1.5 8.5 0.5 1.8 Z"/></svg>
        555.014.2280
      </li>
      <li>
        <svg viewBox="0 0 10 10" aria-hidden="true"><path d="M0.5 2 H9.5 V8 H0.5 Z M1 2.4 L5 5.4 L9 2.4" fill="none" stroke="#3a3a3a" stroke-width="1"/></svg>
        olu@olu.life
      </li>
      <li>
        <svg viewBox="0 0 10 10" aria-hidden="true"><circle cx="5" cy="5" r="4.5"/></svg>
        www.olu.life
      </li>
    </ul>

    <address class="address">
      4120 W Cedar Ridge Rd<br>
      Fairview, AZ 85000 Suite 100
    </address>
    <div class="rule"></div>
    <p class="motto">CBD for wellness&nbsp; CBD for life</p>
  </section>

  <section class="card card--brand" aria-label="Card front, brand name">
    <div class="watercolor-wash" role="img" aria-label="Dark watercolor wash background"></div>
    <div class="wordmark">OLU</div>
    <div class="tagline">Tonics of Vigor</div>
  </section>
</main>
</body>
</html>
```